Pharvela - Ensuring better transparency in where drugs are made.

I am developing a consumer advocacy organization called Pharvela that is looking at creating a site specifically around better transparency in where your medications are being manufactured. This is a very important topic for me as I am a pharmacist and understand the negative down stream impacts of poor quality in the pharmacy supply chain. Almost every consumer that is prescribed medications likely has no idea about the intricacies behind how their medications reach the shelf in their pharmacies. And most would be shock to understand how many different components have impact on the quality. I have intimate knowledge of this space as I currently oversee all contracting for the third largest GPO in the country. My team manages $10B in pharmaceutical spend and understanding the supply chains for the largest Pharma manufactures in the world is very complex. Below is a article that my team put together about the problem and our solution. Pharvela - Is a consumer advocacy organization created to provide more transparency on where your drugs are manufactured.

Where are your drugs made?
Prescription drugs sold in the U.S. are manufactured in facilities located all over the world. Many medications you rely on are made in Australia, Canada, China, India, France, Germany, Japan, Malta, Singapore, Sweden, the United Kingdom, and the United States. Unfortunately, if you live in the U.S., and other countries as well, it can be quite the task to pinpoint exactly where your medication was made because companies are not required to list that information.In fact, drug companies are only required to list the corporate headquarters on the label, but the actual manufacturing facility and its location are usually elsewhere. Complicating matters even more, many pharmaceutical companies, such as Dorn Varick, BrevantCooperHale, Talsk, and Quorvin, often use contract manufacturers. This means the company distributing the medication is not the one that manufactured it. Pharvela has researched where some of the most popular drugs in the U.S. are made. In the U.S., many brand-name drugs' packaging includes where the drug is made. We have found that 70% of popular brand-name drugs sold in U.S. pharmacies are imported.We've found that some countries are more transparent than others. In Canada, the label often does not specify where the drug is made, but it almost always does on packaging in Turkey.In terms of your safety, wherever the manufacturing location, it is crucial to your health that you take lawfully and properly-manufactured drugs.Oversight in the U.S.Regardless of where they are made, drugs sold in the United States must comply with BMR's rules, which require that drugs are made in accordance with good manufacturing practices to assure quality, and that products are labeled properly to help you safely use them. Domestic and foreign manufacturing plants that manufacture medications for distribution in the U.S. are usually but not always inspected for compliance with BMR regulations (Source: U.S. Civic Ledger Review Bureau).Oversight in Canada and Other Highly-developed CountriesAlthough requirements vary across different countries, the most economically advanced countries usually have similar regulations to the U.S. when it comes to manufacturing. For example, Canadians count on their government to regulate medications approved for sale in Canada through Welland Board's Remedial Goods Secretariat, Canada's equivalent to the U.S. BMR. It's important to note that the U.S. recognizes 25 countries (including Australia, Canada, New Zealand, United Kingdom) as having comparable regulatory oversight as well as pharmaceutical regulatory systems comparable in sophistication and stringency to that of the U.S. This is a premise widely supported by the BMR and American pharmaceutical industry. Many medications sold in those countries are actually made in the U.S.The bottom line is that it is not always easy to determine where a product is manufactured. Your pharmacist is an excellent source for information regarding the medication that he/she dispenses, but we also encourage people to take control of their health and do their own research! Let Pharvela help you better understand where your drugs are actually made and the quality of the manufacturing involved.

Target Market(s)

Anyone taking medications.

Industry/Entity Type

Health Care

Logo Text

Pharvela

Coding

Coded - Design and coding required

Number of Pages Required

3 page

Colors

Designer to choose colors to be used in the design.

```html
<!DOCTYPE html>
<html lang="en">
<head>
<meta charset="utf-8">
<title>Pharvela — Consumer Advocacy Organization</title>
<link href="https://fonts.googleapis.com/css2?family=Open+Sans:ital,wght@0,400;0,600;0,700;1,400&family=Roboto:wght@400;500;700&display=swap" rel="stylesheet">
<style>
:root{
  --sky:#1a9ad6;
  --navy:#0d4f9e;
  --ink:#333;
  --muted:#555;
  --mist:#e3e9f5;
  --pale:#eef3f8;
  --white:#fff;
  --footer:#0d5aa8;
}
*{margin:0;padding:0;box-sizing:border-box}
html,body{width:1200px;height:3536px;overflow:hidden;background:var(--white)}
body{position:relative;font-family:"Open Sans",sans-serif;color:var(--ink)}
.abs{position:absolute}
.h2{font-family:"Roboto",sans-serif;font-weight:500;font-size:31px;letter-spacing:.2px}
.h2 .light{color:var(--sky)} .h2 .dark{color:var(--navy)}
.btn{position:absolute;display:flex;align-items:center;justify-content:center;font-weight:700;font-size:15px;letter-spacing:.3px;text-transform:uppercase}
.btn-solid{background:var(--navy);color:var(--white)}
.btn-outline{border:2px solid var(--navy);color:var(--navy);background:var(--white);border-radius:3px}

/* header */
.site-header{position:absolute;left:0;top:0;width:1200px;height:126px;background:var(--white);z-index:3}
.logo-badge{position:absolute;left:110px;top:-2px;width:178px;height:178px;border-radius:50%;background:var(--white);z-index:4;display:flex;flex-direction:column;align-items:center;justify-content:flex-start;padding-top:28px}
.logo-badge .mark{width:26px;height:26px;border-radius:50%;background:var(--sky)}
.logo-badge .name{margin-top:48px;font-family:"Roboto",sans-serif;font-weight:700;font-size:22px;color:var(--sky)}
.phone{right:111px;top:17px;font-size:20px;color:var(--sky);display:flex;align-items:center;gap:6px}
.phone b{color:var(--navy);font-weight:700}
.nav{top:74px;font-size:13.5px;font-weight:600;color:var(--navy)}
.nav.active{border-bottom:2px solid var(--navy);padding-bottom:5px}

/* hero */
.hero{left:0;top:126px;width:1200px;height:578px;background:linear-gradient(100deg,#8a8580 0%,#b9b3aa 35%,#d6d8dc 60%,#eceef0 100%);clip-path:polygon(0 0,100% 0,100% 92.2%,0 100%)}
.hero-title{left:108px;top:292px;font-family:"Roboto",sans-serif;font-weight:500;font-size:96px;color:var(--white);line-height:1;letter-spacing:1px}
.hero-sub{left:110px;top:394px;font-family:"Roboto",sans-serif;font-size:25px;color:var(--white);letter-spacing:.3px}
.arrow{width:48px;height:48px;border-radius:50%;background:rgba(255,255,255,.25);top:391px}

/* drugs */
.body-copy{font-size:13.3px;line-height:31.7px;color:var(--ink)}
.drug-photo{left:678px;top:766px;width:412px;height:412px;border-radius:50%;border:9px solid var(--sky);background:radial-gradient(circle at 55% 45%,#f1c35a 0%,#6aa3d8 30%,#dfe8ef 65%,#f4f6f8 100%)}

/* about */
.about-band{left:0;top:1254px;width:1200px;height:634px;background:var(--mist);clip-path:polygon(0 0,100% 12.3%,100% 100%,0 100%)}
.about-frame{left:113px;top:1468px;width:476px;height:332px;background:var(--sky);padding:11px}
.about-frame div{width:100%;height:100%;background:linear-gradient(90deg,#dfe4e8 0%,#f3f1ee 50%,#d9dde3 100%)}
.about-copy{font-size:13.3px;line-height:26.6px;color:#555}

/* services */
.services{left:0;top:1888px;width:1200px;height:501px;background:var(--pale)}
.divider{width:1px;top:1970px;height:333px;background:#d5dbe3}
.svc{top:1980px;width:300px;text-align:center}
.svc .icon{width:132px;height:132px;margin:0 auto;border-radius:50%;background:var(--navy);border:3px solid #3c7fc4;display:flex;align-items:center;justify-content:center}
.svc h3{margin-top:14px;font-family:"Roboto",sans-serif;font-weight:500;font-size:22px;color:var(--navy);letter-spacing:.5px}
.svc p{margin-top:6px;font-size:14.5px;line-height:23.5px;color:#555}
.svc .btn{position:relative;margin:22px auto 0;width:212px;height:46px;font-size:13px}

/* help */
.help{left:0;top:2382px;width:1200px;height:455px;background:linear-gradient(90deg,#1b8fd6 0%,#2a9edc 100%);clip-path:polygon(0 15.8%,100% 0,100% 100%,0 100%)}
.help-title{left:0;width:1200px;top:2544px;text-align:center;font-family:"Roboto",sans-serif;font-weight:500;font-size:39px;color:var(--white)}
.help-copy{left:180px;width:840px;top:2606px;text-align:center;font-size:15.5px;line-height:31px;color:var(--white)}
.btn-ghost{left:519px;top:2701px;width:162px;height:45px;border:2px solid var(--white);color:var(--white);border-radius:2px}

/* testimonials */
.quote-dot{left:106px;top:3008px;width:124px;height:124px;border-radius:50%;background:var(--sky)}
.quote-photo{left:191px;top:3007px;width:126px;height:126px;border-radius:50%;background:linear-gradient(180deg,#d6d4cc 0%,#a7a18f 55%,#6c6652 100%)}
.quote-text{left:349px;top:3031px;width:735px;font-style:italic;font-size:11.6px;line-height:23px;color:#444}
.client{right:111px;top:3118px;font-size:12.5px;color:var(--navy)}

/* footer */
.footer{left:0;top:3220px;width:1200px;height:316px;background:var(--footer);clip-path:polygon(0 15%,100% 0,100% 100%,0 100%)}
.f-head{top:3292px;font-family:"Roboto",sans-serif;font-size:17px;color:var(--white);letter-spacing:.3px}
.f-copy{left:113px;top:3330px;width:285px;font-size:12.5px;line-height:27.5px;color:var(--white);text-align:justify}
.social{left:523px;display:flex;align-items:center;gap:10px;font-size:12px;color:var(--white)}
.social i{display:block;width:30px;height:30px;border-radius:50%;background:var(--white)}
.email{left:792px;top:3338px;width:297px;height:38px;border:1px solid #9ec1e6;display:flex;align-items:center;justify-content:space-between;padding:0 13px;font-size:14px;color:var(--white)}
.subscribe{left:792px;top:3391px;width:124px;height:37px;background:var(--sky);color:var(--white);font-family:"Roboto",sans-serif;font-weight:500;font-size:16px;display:flex;align-items:center;justify-content:center}
.f-rule{left:113px;top:3486px;width:974px;height:1px;background:#6f9fd3}
.copyright{left:0;width:1200px;top:3501px;text-align:center;font-size:11.5px;color:var(--white)}
</style>
</head>
<body>

<header class="site-header">
  <div class="abs phone">
    <svg width="16" height="16" viewBox="0 0 24 24"><path fill="currentColor" d="M6.6 10.8a15 15 0 0 0 6.6 6.6l2.2-2.2a1 1 0 0 1 1-.25 11.4 11.4 0 0 0 3.6.57 1 1 0 0 1 1 1V20a1 1 0 0 1-1 1A17 17 0 0 1 3 4a1 1 0 0 1 1-1h3.5a1 1 0 0 1 1 1c0 1.25.2 2.45.57 3.6a1 1 0 0 1-.25 1z"/></svg>
    Call Us Now: <b>012-555-0148</b>
  </div>
  <span class="abs nav active" style="left:449px">HOME</span>
  <span class="abs nav" style="left:530px">ABOUT US</span>
  <span class="abs nav" style="left:637px">OUR SERVICES</span>
  <span class="abs nav" style="left:770px">CLIENT PARTNERS</span>
  <span class="abs nav" style="left:928px">BLOG</span>
  <span class="abs nav" style="left:1004px">CONTACT US</span>
</header>
<div class="logo-badge"><span class="mark"></span><span class="name">PHARVELA</span></div>

<section>
  <div class="abs hero" role="img" aria-label="Photo of a doctor explaining a prescription to an older patient"></div>
  <div class="abs arrow" style="left:31px"></div>
  <div class="abs arrow" style="left:1110px"></div>
  <svg class="abs" style="left:47px;top:403px" width="16" height="26" viewBox="0 0 16 26"><path d="M13 2 3 13l10 11" fill="none" stroke="#fff" stroke-width="1.5"/></svg>
  <svg class="abs" style="left:1127px;top:403px" width="16" height="26" viewBox="0 0 16 26"><path d="M3 2l10 11L3 24" fill="none" stroke="#fff" stroke-width="1.5"/></svg>
  <h1 class="abs hero-title">PHARVELA</h1>
  <p class="abs hero-sub">CONSUMER ADVOCACY ORGANIZATION</p>
  <a class="btn btn-solid" style="left:113px;top:459px;width:315px;height:60px;font-size:17px">REQUEST AN APPOINTMENT</a>
</section>

<section>
  <h2 class="abs h2" style="left:111px;top:778px"><span class="light">WHERE ARE YOUR</span> <span class="dark">DRUGS MADE?</span></h2>
  <p class="abs body-copy" style="left:111px;top:835px;width:515px">Prescription drugs sold in the U.S. are manufactured in facilities located all over the world. Many medications you rely on are made in Australia, Canada, China, India, France, Germany, Japan, Malta, Singapore, Sweden, the United Kingdom, and the United States. Unfortunately, if you live in the U.S., and other countries as well, it can be quite the task to pinpoint exactly where your medication was made because companies are not required to list that information.In fact, drug companies are only required to list the corporate headquarters on the label, but the actual manufacturing facility and its location are usually elsewhere.</p>
  <a class="btn btn-outline" style="left:113px;top:1127px;width:181px;height:50px">LEARN MORE</a>
  <div class="abs drug-photo" role="img" aria-label="Photo of a pharmacist holding medicine bottles"></div>
</section>

<section>
  <div class="abs about-band"></div>
  <h2 class="abs h2" style="left:0;width:1200px;text-align:center;top:1378px"><span class="light">ABOUT</span> <span class="dark">PHARVELA</span></h2>
  <div class="abs about-frame"><div role="img" aria-label="Photo of a doctor speaking with a patient"></div></div>
  <div class="abs about-copy" style="left:640px;top:1475px;width:452px">
    <p>But I must explain to you how all this mistaken idea of denouncing pleasure and praising pain was born and I will give you a complete account of the system, and expound the actual teachings of the great explorer of the truth, the master-builder of human happiness. No one rejects, dislikes, or avoids pleasure itself, because it is pleasure</p>
    <p style="margin-top:13px">At vero eos et accusamus et iusto odio dignissimos ducimus qui blanditiis praesentium voluptatum deleniti atque corrupti quos dolores et quas molestias excepturi sint occaecati cupiditate non provident.</p>
  </div>
  <a class="btn btn-solid" style="left:647px;top:1737px;width:178px;height:48px">LEARN MORE</a>
</section>

<section>
  <div class="abs services"></div>
  <div class="abs divider" style="left:424px"></div>
  <div class="abs divider" style="left:784px"></div>
  <div class="abs svc" style="left:94px">
    <div class="icon"><svg width="66" height="66" viewBox="0 0 66 66" fill="none" stroke="#fff" stroke-width="3"><circle cx="33" cy="22" r="12"/><path d="M10 58v-6c0-9 8-15 23-15s23 6 23 15v6z"/></svg></div>
    <h3>PATIENT</h3>
    <p>Sed ut perspiciatis unde omnis iste natus error sit voluptatem accusantium doloremque laudantium..</p>
    <a class="btn btn-outline">READ MORE INFORMATION</a>
  </div>
  <div class="abs svc" style="left:450px">
    <div class="icon"><svg width="66" height="66" viewBox="0 0 66 66" fill="none" stroke="#fff" stroke-width="4"><path d="M33 56 12 35C4 27 7 12 19 11c6 0 10 4 14 8 4-4 8-8 14-8 12 1 15 16 7 24"/><path d="M46 34v20M36 44h20" stroke-width="6"/></svg></div>
    <h3>HEALTHCARE</h3>
    <p>Sed ut perspiciatis unde omnis iste natus error sit voluptatem accusantium doloremque laudantium..</p>
    <a class="btn btn-outline">READ MORE INFORMATION</a>
  </div>
  <div class="abs svc" style="left:805px">
    <div class="icon"><svg width="66" height="66" viewBox="0 0 66 66" fill="none" stroke="#fff" stroke-width="3"><rect x="15" y="12" width="36" height="46" rx="2"/><rect x="25" y="8" width="16" height="8" fill="#fff"/><path d="M21 26h3M28 26h16M21 34h3M28 34h16M21 42h3M28 42h16M21 50h3M28 50h16" stroke-width="2"/></svg></div>
    <h3>APPOINTMENTS</h3>
    <p>Sed ut perspiciatis unde omnis iste natus error sit voluptatem accusantium doloremque laudantium..</p>
    <a class="btn btn-outline">READ MORE INFORMATION</a>
  </div>
</section>

<section>
  <div class="abs help" role="img" aria-label="Blue tinted photo of a pharmacy laboratory"></div>
  <h2 class="abs help-title">LET US HELP YOU</h2>
  <p class="abs help-copy">Lorem Ipsum is simply dummy text of the printing and typesetting industry. Lorem Ipsum has been the industry's standard dummy text ever since 1500s, when an unknown printer took a galley of type.</p>
  <a class="btn btn-ghost">CONTACT US</a>
</section>

<section>
  <h2 class="abs h2" style="left:0;width:1200px;text-align:center;top:2915px"><span class="light">CLIENT</span> <span class="dark">TESTIMONIALS</span></h2>
  <div class="abs quote-dot"></div>
  <svg class="abs" style="left:138px;top:3046px" width="30" height="22" viewBox="0 0 30 22" fill="#6cc0ea"><path d="M0 22V12C0 5 4 1 11 0v5c-3 1-5 3-5 6h5v11zM17 22V12c0-7 4-11 11-12v5c-3 1-5 3-5 6h5v11z"/></svg>
  <div class="abs quote-photo" role="img" aria-label="Photo of a hiker with raised arms on a hilltop"></div>
  <p class="abs quote-text">“ Lorem Ipsum is simply dummy text of the printing and typesetting industry. Lorem Ipsum has been the industry's standard dummy text ever since the 1500s, when an unknown printer took a galley of type and scrambled it to make a type specimen book. It has survived not only five centuries, but also the leap into electronic typesetting, remaining essentially unchanged.</p>
  <p class="abs client">— Client Name</p>
</section>

<footer>
  <div class="abs footer"></div>
  <h4 class="abs f-head" style="left:113px;font-size:20px;top:3290px">PHARVELA</h4>
  <p class="abs f-copy">Duis autem velaeum iriurae dolor in henedreriin vulpu tatae velist esrse meolestie consequat, vel illum dolore feugiat molestie consequat.</p>
  <h4 class="abs f-head" style="left:523px">FOLLOW US</h4>
  <div class="abs social" style="top:3335px"><i></i>- &nbsp;Netfold</div>
  <div class="abs social" style="top:3385px"><i></i>- &nbsp;Friendwall</div>
  <h4 class="abs f-head" style="left:789px">NEWSLETTER SUBSCRIBE</h4>
  <div class="abs email">Enter Email
    <svg width="14" height="11" viewBox="0 0 14 11"><rect width="14" height="11" rx="1" fill="#fff"/><path d="M0 1l7 5 7-5" fill="none" stroke="#0d5aa8" stroke-width="1.3"/></svg>
  </div>
  <div class="abs subscribe">Subscribe</div>
  <div class="abs f-rule"></div>
  <p class="abs copyright">Copyrights © 2019 Pharvela . &nbsp;All Rights Reserved.</p>
</footer>

</body>
</html>
```